REEL HARBOR PRODUCTION SERVICES needs a Brochure Design

We are a new company based in dubai that specializes in creative media production. We create conceptual tv commercials, corporate videos, music videos, documentaries, short films, training videos, time-lapses, we also cover live events and do photography.
We would like the designer to be creative in their design and also provide text to go with.
Link to our logo: http://www.artpitchhub.com/design/482031/logo-design-by-vantor-estudios
We want six pages:
1- Logo with web link at bottom of page
2- About Us
3- Services Offered
4- Equipment List
5- Equipment List continued
6- Contact Us
PS: Use champagne & limousines Font.
Our Address:
Blgd. Al Nakheel Tower, Off. 204, Al Safwa
Dubai, UAE
T: +9714 521 7093
PoBox. 38215
Web: www.reelharbordubai.com
Please do not copy or create exactly the same "About Us" that is found in the attached files. We are looking for something more professional along the same lines.

```html
<!DOCTYPE html>
<html lang="en">
<head>
<meta charset="utf-8">
<title>Reel Harbor Production Services – Contact Us</title>
<link rel="stylesheet" href="https://fonts.googleapis.com/css2?family=Josefin+Sans:wght@300;400;600&display=swap">
<style>
  :root {
    --yellow: #fff200;
    --amber: #fbb616;
    --orange: #f7931e;
    --red: #e8203a;
    --magenta: #ec1b6b;
    --ink: #111111;
    --grey: #3a3a3a;
    --white: #ffffff;
  }
  * { margin: 0; padding: 0; box-sizing: border-box; }
  html, body { width: 1200px; height: 848px; overflow: hidden; background: var(--white); }
  .page {
    position: relative;
    width: 1200px; height: 848px;
    overflow: hidden;
    font-family: "Josefin Sans", sans-serif;
    color: var(--ink);
    background: linear-gradient(to bottom, var(--yellow) 0%, #fffa9a 22%, var(--white) 40%);
  }
  .backdrop { position: absolute; inset: 0; }
  .contact-title {
    position: absolute; left: 198px; top: 58px;
    font-size: 31px; font-weight: 400; color: var(--magenta); letter-spacing: 0.5px;
  }
  .person { position: absolute; left: 76px; width: 448px; }
  .person-name { position: absolute; left: 0; top: 0; font-size: 22px; font-weight: 400; }
  .person-lines {
    position: absolute; right: 0; top: 2px;
    text-align: right; font-size: 15px; font-weight: 300; line-height: 28px;
  }
  .person-lines .email { font-size: 14px; }
  .company {
    position: absolute; right: 680px; top: 458px;
    text-align: right; font-size: 27px; font-weight: 400; line-height: 34px;
    color: var(--magenta);
  }
  .address {
    position: absolute; right: 680px; top: 540px;
    text-align: right; font-size: 17px; font-weight: 400; line-height: 22.5px;
  }
  .brand-mark {
    position: absolute; left: 772px; top: 690px; width: 260px;
    display: flex; align-items: center; gap: 10px;
    font-size: 23px; font-weight: 300; line-height: 26px; color: var(--grey);
  }
  .brand-mark .dot { width: 14px; height: 14px; background: var(--red); flex: none; }
  .web {
    position: absolute; left: 798px; top: 771px;
    font-size: 17px; font-weight: 600; color: var(--magenta);
  }
</style>
</head>
<body>
<main class="page">
  <svg class="backdrop" width="1200" height="848" viewBox="0 0 1200 848" aria-hidden="true">
    <defs>
      <linearGradient id="band" x1="0" y1="0" x2="1" y2="0">
        <stop offset="0" stop-color="#ffe100"/>
        <stop offset="0.45" stop-color="#f99a1e"/>
        <stop offset="1" stop-color="#ee2a45"/>
      </linearGradient>
      <linearGradient id="wedge" x1="0" y1="0" x2="1" y2="0">
        <stop offset="0" stop-color="#f2245a"/>
        <stop offset="0.6" stop-color="#f7931e"/>
        <stop offset="1" stop-color="#fbb616"/>
      </linearGradient>
      <linearGradient id="trail" x1="1" y1="0" x2="0" y2="0">
        <stop offset="0" stop-color="#fbb616" stop-opacity="0.9"/>
        <stop offset="1" stop-color="#fff200" stop-opacity="0"/>
      </linearGradient>
      <linearGradient id="feature" x1="0" y1="0" x2="0.6" y2="1">
        <stop offset="0" stop-color="#e0283a"/>
        <stop offset="0.55" stop-color="#8a1420"/>
        <stop offset="1" stop-color="#f4b41a"/>
      </linearGradient>
    </defs>
    <polygon class="film-band" points="0,462 762,848 0,848" fill="url(#band)"/>
    <polygon class="light-trail" points="520,585 940,505 940,528 520,615" fill="url(#trail)"/>
    <polygon class="accent-wedge" points="940,505 1200,368 1200,505" fill="url(#wedge)"/>
    <rect class="feature-art" role="img" aria-label="Large folded film-strip artwork in red, black and gold" x="752" y="0" width="368" height="530" rx="24" fill="url(#feature)" opacity="0.9"/>
    <line class="dash-rule" x1="0" y1="775" x2="1200" y2="775" stroke="#fff36b" stroke-width="9" stroke-dasharray="9 7" opacity="0.8"/>
  </svg>

  <h1 class="contact-title">CONTACT&nbsp; US</h1>

  <section class="person" style="top:117px">
    <h2 class="person-name">TAREK AMADI</h2>
    <p class="person-lines"><span class="email">tarek@reelharbordubai.com</span><br>+97150 612 48 30<br>+97150 274 19 66</p>
  </section>
  <section class="person" style="top:231px">
    <h2 class="person-name">VIKRAM SOLANKI</h2>
    <p class="person-lines"><span class="email">vik@reelharbordubai.com</span><br>+97150 839 52 07<br>+97155 466 08 91</p>
  </section>
  <section class="person" style="top:345px">
    <h2 class="person-name">NADIM QURESHI</h2>
    <p class="person-lines"><span class="email">nadim@reelharbordubai.com</span><br>+97155 357 21 84<br>+97150 948 63 15</p>
  </section>

  <p class="company">REEL HARBOR<br>PRODUCTION SERVICES</p>
  <address class="address" style="font-style:normal">
    Blgd. Al Nakheel Tower, Off. 204, Al Safwa<br>
    Dubai, UAE<br>
    T: +9714 521 7093<br>
    PoBox. 38215
  </address>

  <div class="brand-mark"><span class="dot"></span><span>REEL HARBOR PRODUCTION SERVICES</span></div>
  <p class="web">www.reelharbordubai.com</p>
</main>
</body>
</html>
```